Business Card & Logo Design Project

I am looking for a slick/simple design for a logo and business card, for a music Producer/Mixer/Engineer.

I'm based in Tokyo, Japan and I help my clients polish up their creation to major radio/TV status. My clients pay me for my taste, sense of balance expertise and creative direction/

Design should give impression of seal of quality, professionalism, and enthusiasm need some sort of a logo like design for "orvelle productions".

Please don't include music notes or instruments or anything musically related and anything samurai or ninja or too much Japan in them on the design.

I like clever, slick stuff that's not too obvious.
I also like a smooth gradation type transition. My favorite color is deep dark blue/

Good Luck and Thank you for your effort.
Updates

I would like a two-sided design for this one.
One side with "orvelle productions" (all lower case) on, and the other side with my name and contact info.

Please also consider portrait position (or direction).  (as opposed to landscape) 

Target Market(s)

My primary targets are artists & bands, who want absolute best for their creation.

Industry/Entity Type

Business

Requirements
Must have
• Two-Sided
1, orvelle productions
2, Kenji Harumoto, Producer/Mixer/Engineer, +81 090 4827 3516, brambleway@mailnest.example
Nice to have
• Any suggestions are welcome//
Should not have
• Anything music related images.
(e.g. CD, music notations, instruments etc.)

```html
<!DOCTYPE html>
<html lang="en">
<head>
<meta charset="utf-8">
<title>orvelle productions – business card</title>
<link rel="stylesheet" href="https://fonts.googleapis.com/css2?family=Open+Sans:wght@600;700&display=swap">
<style>
  :root {
    --page-bg: #2b2b2d;
    --card-light: #1f5c80;
    --card-mid: #134265;
    --card-dark: #0a2640;
    --band-white: #ffffff;
    --ink-navy: #0e2a47;
    --ink-dark: #1c1c1c;
    --card-shadow: rgba(0, 0, 0, 0.55);
  }
  * { margin: 0; padding: 0; box-sizing: border-box; }
  html, body {
    width: 1200px;
    height: 900px;
    overflow: hidden;
    background: var(--page-bg);
    font-family: "Open Sans", Arial, sans-serif;
  }
  .canvas {
    position: relative;
    width: 1200px;
    height: 900px;
  }
  .card {
    position: absolute;
    width: 620px;
    height: 385px;
    background: radial-gradient(ellipse at 62% 42%, var(--card-light) 0%, var(--card-mid) 45%, var(--card-dark) 100%);
    box-shadow: 0 14px 30px var(--card-shadow);
    overflow: hidden;
  }
  .card--front { left: 50px; top: 50px; }
  .card--back  { left: 530px; top: 465px; }

  .brand-block {
    position: absolute;
    left: 0;
    top: 26px;
    width: 290px;
    height: 104px;
    background: var(--band-white);
    display: flex;
    align-items: center;
    padding-left: 24px;
  }
  .brand-name {
    font-weight: 700;
    font-size: 23px;
    color: var(--ink-navy);
    letter-spacing: 0.3px;
    white-space: nowrap;
  }

  .band {
    position: absolute;
    left: 0;
    background: var(--band-white);
    display: flex;
    align-items: center;
    padding-left: 30px;
    color: var(--ink-navy);
    font-weight: 700;
    white-space: nowrap;
  }
  .band--name  { top: 160px; width: 300px; height: 42px; font-size: 24px; }
  .band--title { top: 207px; width: 300px; height: 26px; font-size: 13px; color: var(--ink-dark); }
  .band--blank { top: 262px; width: 312px; height: 24px; }
  .band--phone { top: 291px; width: 312px; height: 24px; font-size: 13px; color: var(--ink-dark); }
  .band--email { top: 320px; width: 312px; height: 26px; font-size: 13px; color: var(--ink-dark); padding-left: 24px; }

  .back-brand {
    position: absolute;
    inset: 0;
    display: flex;
    align-items: center;
    justify-content: center;
  }
  .back-brand .brand-name {
    color: var(--band-white);
    font-size: 30px;
  }
</style>
</head>
<body>
  <main class="canvas">
    <section class="card card--front" aria-label="Card front with contact details">
      <div class="brand-block">
        <span class="brand-name">orvelle productions</span>
      </div>
      <div class="band band--name">Kenji Harumoto</div>
      <div class="band band--title">Producer/Mixer/Engineer</div>
      <div class="band band--blank"></div>
      <div class="band band--phone">+81 090 4827 3516</div>
      <div class="band band--email">brambleway@mailnest.example</div>
    </section>

    <section class="card card--back" aria-label="Card back with company name">
      <div class="back-brand">
        <span class="brand-name">orvelle productions</span>
      </div>
    </section>
  </main>
</body>
</html>
```